New Website Design for Rides for Heroes.org - A Site for People to Donate Cars to War / Disabled Ve

Current site: www.ridesforheroes.org; Look at these sites for ideas: bikez2tots.org; gearsforhopes.org; www.autosformarines.org; www.trucksforsoldiers.org

Industry/Entity Type

Charity

Coding

Coded - Design and coding required

Number of Pages Required

1 page

Requirements
Must have
• n/a
Nice to have
• n/a
Should not have
• n/a

```html
<!DOCTYPE html>
<html lang="en">
<head>
<meta charset="utf-8">
<title>Rides for Heroes</title>
<link href="https://fonts.googleapis.com/css2?family=Lato:wght@400;700;900&family=Open+Sans:ital,wght@0,400;0,600;1,400&display=swap" rel="stylesheet">
<style>
:root{
  --blue:#0d5fa6;
  --blue-dark:#0a4a85;
  --blue-deep:#0b3f73;
  --nav-active:#4a3f3b;
  --text:#444;
  --panel:#3a3a3a;
  --grey-band:#f2f2f2;
  --footer:#2b2b2b;
  --white:#fff;
}
*{box-sizing:border-box;margin:0;padding:0}
html,body{width:802px;height:1200px;overflow:hidden;background:var(--white)}
body{position:relative;font-family:"Open Sans",sans-serif;color:var(--text);font-size:8px}
.abs{position:absolute}
.top-line{left:0;top:0;width:802px;height:3px;background:var(--blue)}
.brand{left:66px;top:16px;display:flex;align-items:center;gap:6px}
.brand-mark{width:18px;height:18px;border-radius:50%;background:var(--blue)}
.brand-name{font-family:"Lato",sans-serif;font-weight:900;color:var(--blue);font-size:17px;line-height:1;letter-spacing:.5px}
.brand-sub{font-family:"Lato",sans-serif;font-weight:900;color:var(--blue);font-size:10px;letter-spacing:.5px;margin-top:2px}
.header-box{top:25px;height:38px;border:1px solid #e3e3e3;border-radius:3px;padding:7px 10px;display:flex;align-items:center;justify-content:space-between}
.header-box small{display:block;font-size:6px;color:#555;text-transform:uppercase}
.header-box b{display:block;font-weight:400;font-size:10px;color:var(--blue);margin-top:2px}
.header-box .dot{width:20px;height:20px;border-radius:50%;background:#d9b44a}
.header-box .dot.agent{background:#c9c9c9}
.nav{left:0;top:86px;width:802px;height:32px;background:var(--blue)}
.nav ul{list-style:none;position:absolute;left:66px;top:0;display:flex;height:32px}
.nav li{color:var(--white);font-size:8.5px;display:flex;align-items:center;justify-content:center;border-right:1px solid rgba(255,255,255,.15)}
.nav li.active{background:var(--nav-active)}
.hero{left:0;top:118px;width:802px;height:288px;background:linear-gradient(90deg,#e9e4e4 0%,#d9d3cf 25%,#6b6148 45%,#5a553f 60%,#cfcfcf 80%,#e6e6e6 100%)}
.hero-copy{left:65px;top:213px}
.hero-copy .tag{font-style:italic;font-size:7.5px;color:var(--blue)}
.hero-copy h1{font-family:"Lato",sans-serif;font-weight:700;font-size:16px;color:var(--blue);margin-top:4px}
.hero-copy p{font-size:8.5px;color:#333;width:260px;line-height:1.4;margin-top:2px}
.btn{display:inline-flex;align-items:center;justify-content:center;background:var(--blue);color:var(--white);font-family:"Lato",sans-serif;font-weight:700;font-size:8px;border-radius:2px}
.arrow{top:240px;width:14px;height:36px}
.donate-form{left:557px;top:134px;width:178px;height:234px;background:var(--panel)}
.donate-form h2{height:29px;background:var(--blue);color:var(--white);font-family:"Lato",sans-serif;font-weight:700;font-size:13px;padding:8px 11px;letter-spacing:.3px}
.field{margin:8px 9px 0;height:23px;border:1px solid #6c6c6c;border-radius:2px;color:#c9c9c9;font-size:8px;padding:5px 10px;display:flex;justify-content:space-between}
.donate-form .btn{margin:9px 0 0 10px;width:79px;height:26px;font-size:7.5px}
.feature{top:396px;height:44px;background:linear-gradient(#1a6db6,var(--blue-dark));color:var(--white);display:flex;align-items:center;gap:14px;padding-left:40px;font-family:"Lato",sans-serif;font-weight:700;font-size:9.5px}
.why h2,.program h2,.today h2,.secure h2{font-family:"Lato",sans-serif;font-weight:700;color:var(--blue)}
.why{left:66px;top:466px;width:400px}
.why h2{font-size:19px}
.why ul,.today ul{list-style:none}
.why li{display:flex;gap:9px;font-size:7.5px;line-height:1.7;color:#555;margin-top:7px}
.why li b{font-weight:600;color:#333}
.tick{flex:0 0 8px;margin-top:3px}
.photo{border:3px solid var(--white);box-shadow:0 0 0 1px #ccc}
.program{left:0;top:681px;width:802px;height:231px;background:var(--grey-band);border-top:1px solid #e6e6e6;border-bottom:1px solid #e6e6e6}
.program h2{position:absolute;top:27px;width:100%;text-align:center;font-size:19px;padding-left:80px}
.step{top:759px;width:84px;height:84px;border-radius:50%;border:1.5px solid var(--blue);display:flex;align-items:center;justify-content:center;background:var(--grey-band)}
.step.first{background:linear-gradient(#1a6db6,var(--blue-deep));border:none}
.step-label{top:852px;width:130px;text-align:center;font-size:8px;color:#555;line-height:1.7}
.link-bar{top:797px;height:6px;background:#d8d8d8}
.link-head{top:792px;width:0;height:0;border-top:8px solid transparent;border-bottom:8px solid transparent;border-left:10px solid #d0d0d0}
.today{left:299px;top:946px}
.today h2{font-size:14px}
.today li{display:flex;gap:12px;font-size:7.5px;color:#555;margin-top:7px;line-height:1.6}
.secure{left:501px;top:946px;width:236px;height:155px;border:1px solid #ddd;padding:10px 13px}
.secure h2{font-size:14px}
.secure p{font-size:7.5px;line-height:2.5;color:#555;margin-top:4px}
.badges{display:flex;gap:6px;align-items:center;margin-top:6px}
.footer{left:0;top:1129px;width:802px;height:71px;background:var(--footer);color:#ddd}
.footer nav{position:absolute;left:65px;top:22px;font-size:8px;display:flex;gap:17px}
.footer p{position:absolute;left:66px;top:44px;font-size:8px}
.social{position:absolute;top:27px;display:flex;gap:2px;left:641px}
.social span{width:22px;height:22px;border-radius:50%}
</style>
</head>
<body>
<div class="abs top-line"></div>

<div class="abs brand">
  <span class="brand-mark"></span>
  <div><div class="brand-name">RIDES</div><div class="brand-sub">FOR HEROES</div></div>
</div>
<div class="abs header-box" style="left:470px;width:128px"><div><small>Members</small><b>Login / Register</b></div><span class="dot"></span></div>
<div class="abs header-box" style="left:608px;width:127px"><div><small>We need your help</small><b>1-800-555-0142</b></div><span class="dot agent"></span></div>

<nav class="abs nav"><ul>
  <li class="active" style="width:109px">Home</li>
  <li style="width:95px">About</li>
  <li style="width:152px">How to Donate your Vehicle</li>
  <li style="width:103px">FAQ</li>
  <li style="width:101px">Testimonials</li>
  <li style="width:109px">Contact</li>
</ul></nav>

<div class="abs hero" role="img" aria-label="Photo of a uniformed veteran with a prosthetic leg beside an American flag"></div>
<svg class="abs arrow" style="left:24px" viewBox="0 0 14 36"><path d="M12 1 2 18l10 17" fill="none" stroke="#fff" stroke-width="1"/></svg>
<svg class="abs arrow" style="left:764px" viewBox="0 0 14 36"><path d="M2 1l10 17L2 35" fill="none" stroke="#fff" stroke-width="1"/></svg>
<div class="abs hero-copy">
  <div class="tag">Free 24/7 Pickup with No DMV Hassles.</div>
  <h1>Donate cars to war disabled men</h1>
  <p>We will pick up your car donation, running or not, when it's most convenient, at home or work.</p>
  <span class="btn" style="width:94px;height:27px;margin-top:9px">Request a Quote</span>
</div>

<form class="abs donate-form">
  <h2>DONATE HERE</h2>
  <div class="field">Enter your name</div>
  <div class="field">Email address</div>
  <div class="field">Phone Number</div>
  <div class="field">Address</div>
  <div class="field">State <span>⌄</span></div>
  <span class="btn">DONATE NOW</span>
</form>

<div class="abs feature" style="left:65px;width:219px">
  <svg width="18" height="18" viewBox="0 0 24 24"><path fill="#fff" d="M6.6 10.8a15 15 0 0 0 6.6 6.6l2.2-2.2c.3-.3.7-.4 1-.2 1.1.4 2.3.6 3.6.6.6 0 1 .4 1 1V20c0 .6-.4 1-1 1A17 17 0 0 1 3 4c0-.6.4-1 1-1h3.5c.6 0 1 .4 1 1 0 1.3.2 2.5.6 3.6.1.3 0 .7-.2 1z"/></svg>CALL US</div>
<div class="abs feature" style="left:291px;width:220px;padding-left:24px">
  <svg width="38" height="26" viewBox="0 0 38 26" fill="none" stroke="#fff" stroke-width="1.8"><path d="M20 6h8l6 8v6H20zM20 20H4M6 4l10 14M4 4h4"/><circle cx="9" cy="21" r="3"/><circle cx="28" cy="21" r="3"/></svg>WE TOW IT</div>
<div class="abs feature" style="left:514px;width:220px;padding-left:30px">
  <svg width="26" height="16" viewBox="0 0 26 16"><rect x="1" y="1" width="24" height="14" fill="none" stroke="#fff" stroke-width="2"/><circle cx="13" cy="8" r="4" fill="#fff"/></svg>TAX WRITE OFF</div>

<section class="abs why">
  <h2>Why Donate Your Car to Us?</h2>
  <ul style="margin-top:8px">
    <li><svg class="tick" viewBox="0 0 10 8"><path d="M1 4l3 3 5-6" fill="none" stroke="#0d5fa6" stroke-width="2"/></svg><span><b>Top A+ Rated &amp; IRS 501(c)3 Approved:</b> Free 24/7 Pickup with No DMV Hassles.</span></li>
    <li><svg class="tick" viewBox="0 0 10 8"><path d="M1 4l3 3 5-6" fill="none" stroke="#0d5fa6" stroke-width="2"/></svg><span style="width:370px"><b>Free Local Towing:</b> We will pick up your car donation, running or not, when it's most convenient, at home or work.</span></li>
    <li><svg class="tick" viewBox="0 0 10 8"><path d="M1 4l3 3 5-6" fill="none" stroke="#0d5fa6" stroke-width="2"/></svg><span><b>Top A+ Rated &amp; IRS 501(c)3 Approved:</b> Free 24/7 Pickup with No DMV Hassles.</span></li>
    <li><svg class="tick" viewBox="0 0 10 8"><path d="M1 4l3 3 5-6" fill="none" stroke="#0d5fa6" stroke-width="2"/></svg><span><b>All Cars Accepted:</b> We take your car regardless of its condition or registration status.</span></li>
  </ul>
  <span class="btn" style="width:113px;height:31px;margin-top:20px;background:linear-gradient(#1a6db6,var(--blue-deep))">View more info</span>
</section>
<div class="abs photo" style="left:514px;top:470px;width:215px;height:155px;background:linear-gradient(135deg,#b8c2d2,#d9d3cc 50%,#7d7a66)" role="img" aria-label="Photo of a soldier in camouflage seated in a wheelchair before an American flag"></div>

<section class="abs program"><h2>Car Donation Program</h2></section>
<div class="abs link-bar" style="left:190px;width:70px"></div>
<div class="abs link-head" style="left:260px"></div>
<div class="abs link-bar" style="left:355px;width:70px"></div>
<div class="abs link-head" style="left:425px"></div>
<div class="abs link-bar" style="left:520px;width:73px"></div>
<div class="abs link-head" style="left:593px"></div>
<div class="abs step first" style="left:106px"><svg width="22" height="22" viewBox="0 0 24 24"><path fill="#fff" d="M12 2a7 7 0 0 0-7 7c0 5 7 13 7 13s7-8 7-13a7 7 0 0 0-7-7zm0 9.5A2.5 2.5 0 1 1 12 6.5a2.5 2.5 0 0 1 0 5z"/></svg></div>
<div class="abs step" style="left:271px"><svg width="28" height="20" viewBox="0 0 28 20" fill="#9a9a9a"><path d="M5 8l3-6h12l3 6h3v7h-3v3h-4v-3H10v3H6v-3H2V8z"/><circle cx="8" cy="11" r="2" fill="#f2f2f2"/><circle cx="20" cy="11" r="2" fill="#f2f2f2"/></svg></div>
<div class="abs step" style="left:436px"><svg width="26" height="16" viewBox="0 0 26 16"><rect x="1" y="1" width="24" height="14" fill="none" stroke="#9a9a9a" stroke-width="2"/><circle cx="13" cy="8" r="4" fill="#9a9a9a"/></svg></div>
<div class="abs step" style="left:603px"><svg width="36" height="26" viewBox="0 0 38 26" fill="none" stroke="#9a9a9a" stroke-width="1.8"><path d="M20 6h8l6 8v6H20zM20 20H4M6 4l10 14M4 4h4"/><circle cx="9" cy="21" r="3"/><circle cx="28" cy="21" r="3"/></svg></div>
<div class="abs step-label" style="left:86px">DONATIONS ACCEPTED<br>NATION WIDE</div>
<div class="abs step-label" style="left:252px">ALL VECHICLE TYPES<br>WELCOME</div>
<div class="abs step-label" style="left:414px">TEX DEDUCTIBLE</div>
<div class="abs step-label" style="left:581px">TOWING IS FREE</div>

<div class="abs photo" style="left:68px;top:946px;width:214px;height:155px;background:linear-gradient(135deg,#9aa3ad,#d8cfc6 50%,#4b4e55)" role="img" aria-label="Photo of a smiling couple holding car keys at a dealership"></div>
<section class="abs today">
  <h2>Donate Your Car Today!</h2>
  <ul style="margin-top:3px">
    <li><svg class="tick" viewBox="0 0 10 8"><path d="M1 4l3 3 5-6" fill="none" stroke="#555" stroke-width="2"/></svg>You have no costs.</li>
    <li><svg class="tick" viewBox="0 0 10 8"><path d="M1 4l3 3 5-6" fill="none" stroke="#555" stroke-width="2"/></svg>Free towing, running or not.</li>
    <li><svg class="tick" viewBox="0 0 10 8"><path d="M1 4l3 3 5-6" fill="none" stroke="#555" stroke-width="2"/></svg>We issue you an IRS tax receipt.</li>
    <li><svg class="tick" viewBox="0 0 10 8"><path d="M1 4l3 3 5-6" fill="none" stroke="#555" stroke-width="2"/></svg>We take care of all paperwork.</li>
    <li><svg class="tick" viewBox="0 0 10 8"><path d="M1 4l3 3 5-6" fill="none" stroke="#555" stroke-width="2"/></svg>And we take care of DMV &amp; Smog issues.</li>
  </ul>
  <span class="btn" style="width:113px;height:31px;margin-top:10px;background:linear-gradient(#1a6db6,var(--blue-deep))">Meet our clients</span>
</section>
<section class="abs secure">
  <h2>Safe &amp; Secure</h2>
  <p>Are you in the market for a new car, truck or SUV and want to make sure that you are getting the best deal available? Then you need to know what</p>
  <div class="badges">
    <span style="width:64px;height:22px;background:var(--blue)"></span>
    <span style="width:20px;height:20px;border-radius:50%;background:#1f7ea0"></span>
    <span style="width:36px;height:30px;border-radius:50%;background:#b9c9d8"></span>
    <span style="width:70px;height:24px;background:#c8c8c8"></span>
  </div>
</section>

<footer class="abs footer">
  <nav><span>Home</span><span>/</span><span>About</span><span>/</span><span>How to Donate your Vehicle</span><span>/</span><span>FAQ</span><span>/</span><span>Testimonials</span><span>/</span><span>Contact</span></nav>
  <p>© 2016 ridesforheroes.All rights reserved</p>
  <div class="social"><span style="background:#3b5a9a"></span><span style="background:#2fa8e0"></span><span style="background:#1b75a8"></span><span style="background:#d23b2e"></span></div>
</footer>
</body>
</html>
```